Business Card Design Project

Im an electrician and my company name is Kestrel Electrical
My main work is installing Lighting and Power Points, Home Theater Systems, TVS, Phones and Data
Im looking a business card, something nice, clean, modern and not to cluttered
Im open to sugestions
I dont mind if the "Services" is on the back on the business card
colours black, grey, white or the blue colour of my logo are prefered but not compulsory
any questions just message me
and please make it so if i need to edit the writing can do it easy. maybe by making it a seperate layer ?
My Details are.
Name - Peter Halloran
Job Title - Licenced Electrician
Mobile - 027 583 2174
Email - peter@kestrelelectrical.co.nz
Web - www.kestrelelectrical.co.nz
Services
Residential / Commercial
Lighting & Power
Heating & Ventilation
Automation
Phone & Data
Home Cinema
Sound Systems
TV, Antenna & Satellite
Digital Upgrades

```html
<!DOCTYPE html>
<html lang="en">
<head>
<meta charset="utf-8">
<title>Kestrel Electrical – Business Card</title>
<link href="https://fonts.googleapis.com/css2?family=Source+Sans+3:wght@400;600;700&display=swap" rel="stylesheet">
<style>
  :root {
    --ink: #000000;
    --brand-blue: #02b3cd;
    --faint-blue: #6fd0e0;
    --white: #ffffff;
    --backdrop: #eeeeee;
  }
  * { margin: 0; padding: 0; box-sizing: border-box; }
  html, body { width: 1200px; height: 1000px; overflow: hidden; }
  body {
    background: var(--backdrop);
    font-family: "Source Sans 3", "Myriad Pro", Arial, sans-serif;
    position: relative;
  }
  .card {
    position: absolute;
    top: 350px;
    width: 535px;
    height: 300px;
    overflow: hidden;
    box-shadow: 0 4px 10px rgba(0,0,0,0.25);
  }

  /* Front */
  .card-front { left: 47px; background: var(--ink); }
  .brand {
    position: absolute;
    top: 58px;
    left: 0;
    width: 100%;
    display: flex;
    align-items: center;
    justify-content: center;
    gap: 10px;
  }
  .brand-mark { width: 26px; height: 26px; background: var(--brand-blue); }
  .brand-name {
    color: var(--brand-blue);
    font-weight: 700;
    font-size: 22px;
    letter-spacing: 1px;
    text-transform: uppercase;
  }
  .info-band {
    position: absolute;
    left: 0;
    top: 159px;
    width: 100%;
    height: 90px;
    background: var(--brand-blue);
  }
  .holder {
    position: absolute;
    left: 0;
    top: 17px;
    width: 235px;
    text-align: center;
    color: var(--ink);
  }
  .holder-name { font-size: 23px; font-weight: 600; line-height: 1.1; }
  .holder-title { font-size: 19px; font-weight: 400; line-height: 1.2; }
  .contacts {
    position: absolute;
    left: 273px;
    top: 6px;
    list-style: none;
  }
  .contacts li {
    display: flex;
    align-items: center;
    gap: 8px;
    height: 28.5px;
    font-size: 15.5px;
    color: var(--ink);
  }
  .contacts svg { width: 20px; height: 20px; flex: none; }

  /* Back */
  .card-back {
    left: 618px;
    background: var(--brand-blue);
    border-top: 12px solid var(--ink);
    border-bottom: 11px solid var(--ink);
  }
  .back-brand {
    position: absolute;
    left: 60px;
    top: 118px;
    color: var(--faint-blue);
    font-weight: 700;
    font-size: 34px;
    letter-spacing: 1px;
    text-transform: uppercase;
  }
  .services {
    position: absolute;
    left: 295px;
    top: 10px;
    color: var(--white);
  }
  .services-heading { font-size: 17.5px; font-weight: 700; line-height: 1.4; margin-bottom: 2px; }
  .services-list { list-style: none; }
  .services-list li { font-size: 17.5px; line-height: 28.5px; }
  .services-list li::before { content: "• "; }
</style>
</head>
<body>

<section class="card card-front" aria-label="Business card front">
  <div class="brand">
    <span class="brand-mark"></span>
    <span class="brand-name">Kestrel Electrical</span>
  </div>
  <div class="info-band">
    <div class="holder">
      <p class="holder-name">Peter Halloran</p>
      <p class="holder-title">Licenced Electrician</p>
    </div>
    <ul class="contacts">
      <li>
        <svg viewBox="0 0 20 20" aria-hidden="true"><circle cx="10" cy="10" r="9" fill="none" stroke="#000" stroke-width="1.4"/><rect x="7" y="4.5" width="6" height="11" rx="1" fill="none" stroke="#000" stroke-width="1.4"/><rect x="8.2" y="6" width="3.6" height="5" fill="#000"/></svg>
        <span>027 583 2174</span>
      </li>
      <li>
        <svg viewBox="0 0 20 20" aria-hidden="true"><circle cx="10" cy="10" r="9" fill="none" stroke="#000" stroke-width="1.4"/><rect x="5" y="6.5" width="10" height="7" fill="none" stroke="#000" stroke-width="1.4"/><path d="M5 6.5 L10 10.5 L15 6.5" fill="none" stroke="#000" stroke-width="1.4"/></svg>
        <span>peter@kestrelelectrical.co.nz</span>
      </li>
      <li>
        <svg viewBox="0 0 20 20" aria-hidden="true"><circle cx="10" cy="10" r="9" fill="none" stroke="#000" stroke-width="1.4"/><ellipse cx="10" cy="10" rx="4" ry="9" fill="none" stroke="#000" stroke-width="1.2"/><path d="M1 10 H19 M2.5 5.5 H17.5 M2.5 14.5 H17.5" stroke="#000" stroke-width="1.2"/></svg>
        <span>www.kestrelelectrical.co.nz</span>
      </li>
    </ul>
  </div>
</section>

<section class="card card-back" aria-label="Business card back">
  <p class="back-brand">Kestrel</p>
  <div class="services">
    <h2 class="services-heading">Residential / Commercial</h2>
    <ul class="services-list">
      <li>Lighting &amp; Power</li>
      <li>Heating &amp; Ventilation</li>
      <li>Automation</li>
      <li>Phone &amp; Data</li>
      <li>Home Cinema</li>
      <li>Sound Systems</li>
      <li>TV, Antenna &amp; Satellite</li>
      <li>Digital Upgrades</li>
    </ul>
  </div>
</section>

</body>
</html>
```